Business Card Design Project

I help solve problems that people have with real estate, so I buy homes for cash that they no longer want, can't afford, inherited, etc. and fix and sell them or rent them or take over mortgage payments. See website: www.quickdeedhomestead.com

Industry/Entity Type

Real Estate

Contact Information for Business Card

Not exactly sure. Looking for a design that either is similar to the website www.quickdeedhomestead.com or that reflects what I do as described below. If it can look a little luxurious to show I can buy the houses for cash and I fix them and sell them, it's a bonus. I seem to like some of the higher end things like foil or black or something that makes it stand out.

Font styles to use
Serif

Requirements
Nice to have
• I seem to like black or clear. I like things to stand out and be different.

```html
<!DOCTYPE html>
<html lang="en">
<head>
<meta charset="utf-8">
<title>Renewed Doorways – Business Cards</title>
<link rel="stylesheet" href="https://fonts.googleapis.com/css2?family=Lato:wght@400;900&display=swap">
<style>
  :root {
    --backdrop: #e9ebee;
    --card-white: #ffffff;
    --card-black: #050505;
    --green-light: #6aab45;
    --green-dark: #4a8734;
    --brand-green: #4f9a2f;
    --text-white: #ffffff;
  }
  * { box-sizing: border-box; margin: 0; padding: 0; }
  html, body {
    width: 1200px; height: 1000px; overflow: hidden;
    background: var(--backdrop);
    font-family: "Lato", Arial, sans-serif;
  }
  .sheet { position: relative; width: 1200px; height: 1000px; }

  .card { position: absolute; width: 514px; height: 292px; overflow: hidden; }
  .card--rounded { border-radius: 28px; }
  .card--front-rounded { left: 66px; top: 102px; }
  .card--back-rounded { left: 66px; top: 449px; }
  .card--front-square { left: 624px; top: 266px; }
  .card--back-square { left: 624px; top: 607px; }

  .card-front {
    background: var(--card-white);
    display: flex; align-items: center; justify-content: center;
  }
  .front-wordmark {
    font-weight: 900; font-size: 40px; line-height: 1.0;
    color: var(--brand-green); text-transform: uppercase;
    text-align: center; letter-spacing: 0.5px;
  }

  .card-back { background: var(--card-black); }
  .back-shape { position: absolute; inset: 0; width: 100%; height: 100%; }

  .person-name {
    position: absolute; left: 27px; top: 52px;
    color: var(--text-white); font-size: 28px; font-weight: 400;
  }
  .person-title {
    position: absolute; left: 27px; top: 90px;
    color: var(--text-white); font-size: 15px;
  }
  .contact-list { position: absolute; left: 27px; top: 180px; list-style: none; }
  .contact-item {
    display: flex; align-items: center; gap: 18px;
    color: var(--text-white); font-size: 19px; height: 28px;
  }
  .contact-icon { width: 14px; height: 14px; fill: var(--text-white); }

  .back-wordmark {
    position: absolute; left: 300px; top: 188px; width: 150px;
    color: var(--text-white); font-weight: 900; font-size: 19px;
    line-height: 1.05; text-transform: uppercase; text-align: center;
  }
  .back-website {
    position: absolute; left: 268px; top: 247px; width: 210px;
    color: var(--text-white); font-size: 14.5px; text-align: center;
  }
</style>
</head>
<body>
<main class="sheet">

  <section class="card card--rounded card--front-rounded card-front">
    <p class="front-wordmark">Renewed<br>Doorways</p>
  </section>

  <section class="card card--front-square card-front">
    <p class="front-wordmark">Renewed<br>Doorways</p>
  </section>

  <section class="card card--rounded card--back-rounded card-back">
    <svg class="back-shape" viewBox="0 0 514 292" preserveAspectRatio="none" aria-hidden="true">
      <defs>
        <linearGradient id="greenPanelA" x1="0" y1="0" x2="1" y2="0">
          <stop offset="0" stop-color="var(--green-light)"/>
          <stop offset="1" stop-color="var(--green-dark)"/>
        </linearGradient>
      </defs>
      <path d="M290,0 C345,60 300,135 268,200 C250,240 250,270 262,292 L514,292 L514,0 Z" fill="#ffffff"/>
      <path d="M322,0 C368,62 325,140 294,202 C276,242 266,272 268,292 L514,292 L514,0 Z" fill="url(#greenPanelA)"/>
    </svg>
    <h2 class="person-name">Name of Person</h2>
    <p class="person-title">Title of Person</p>
    <ul class="contact-list">
      <li class="contact-item">
        <svg class="contact-icon" viewBox="0 0 24 24" aria-hidden="true"><path d="M6.6 10.8c1.4 2.8 3.8 5.1 6.6 6.6l2.2-2.2c.3-.3.7-.4 1-.2 1.1.4 2.3.6 3.6.6.6 0 1 .4 1 1V20c0 .6-.4 1-1 1C10.6 21 3 13.4 3 4c0-.6.4-1 1-1h3.5c.6 0 1 .4 1 1 0 1.3.2 2.5.6 3.6.1.3 0 .7-.2 1z"/></svg>
        <span>+123 456 7890</span>
      </li>
      <li class="contact-item">
        <svg class="contact-icon" viewBox="0 0 24 24" aria-hidden="true"><path d="M2 5h20v2l-10 6L2 7zM2 9l10 6 10-6v10H2z"/></svg>
        <span>E-mail Address</span>
      </li>
    </ul>
    <p class="back-wordmark">Renewed<br>Doorways</p>
    <p class="back-website">www.quickdeedhomestead.com</p>
  </section>

  <section class="card card--back-square card-back">
    <svg class="back-shape" viewBox="0 0 514 292" preserveAspectRatio="none" aria-hidden="true">
      <defs>
        <linearGradient id="greenPanelB" x1="0" y1="0" x2="1" y2="0">
          <stop offset="0" stop-color="var(--green-light)"/>
          <stop offset="1" stop-color="var(--green-dark)"/>
        </linearGradient>
      </defs>
      <path d="M290,0 C345,60 300,135 268,200 C250,240 250,270 262,292 L514,292 L514,0 Z" fill="#ffffff"/>
      <path d="M322,0 C368,62 325,140 294,202 C276,242 266,272 268,292 L514,292 L514,0 Z" fill="url(#greenPanelB)"/>
    </svg>
    <h2 class="person-name">Name of Person</h2>
    <p class="person-title">Title of Person</p>
    <ul class="contact-list">
      <li class="contact-item">
        <svg class="contact-icon" viewBox="0 0 24 24" aria-hidden="true"><path d="M6.6 10.8c1.4 2.8 3.8 5.1 6.6 6.6l2.2-2.2c.3-.3.7-.4 1-.2 1.1.4 2.3.6 3.6.6.6 0 1 .4 1 1V20c0 .6-.4 1-1 1C10.6 21 3 13.4 3 4c0-.6.4-1 1-1h3.5c.6 0 1 .4 1 1 0 1.3.2 2.5.6 3.6.1.3 0 .7-.2 1z"/></svg>
        <span>+123 456 7890</span>
      </li>
      <li class="contact-item">
        <svg class="contact-icon" viewBox="0 0 24 24" aria-hidden="true"><path d="M2 5h20v2l-10 6L2 7zM2 9l10 6 10-6v10H2z"/></svg>
        <span>E-mail Address</span>
      </li>
    </ul>
    <p class="back-wordmark">Renewed<br>Doorways</p>
    <p class="back-website">www.quickdeedhomestead.com</p>
  </section>

</main>
</body>
</html>
```